VEKRA Motorcycle Ad

We import a range of specialised high end competition Off-Road motorcycles from Spain. We have a new model out called the VEKRA Dz340e which we would like a banner ad for. The main features we want to highlight on the new VEKRA is the light weight (lightest on the market) BRATTEK rear shock (Best on the market) & an industry leading 2 year warranty. We can supply images etc. tis is our first time using this service so not sure of the procedure.

```html
<!DOCTYPE html>
<html lang="en">
<head>
<meta charset="utf-8">
<title>VEKRA Dz340e Banner</title>
<link rel="stylesheet" href="https://fonts.googleapis.com/css2?family=Roboto:ital,wght@1,700;1,900&display=swap">
<style>
  :root {
    --green: #6fcf6a;
    --green-light: #a6e89f;
    --green-dark: #3f9a3a;
    --ink: #000000;
    --paper: #ffffff;
    --swoosh: #b9b9b9;
    --photo-a: #f4f6f4;
    --photo-b: #cfd5cf;
  }
  html, body {
    margin: 0;
    padding: 0;
    width: 1200px;
    height: 900px;
    overflow: hidden;
    background: var(--paper);
  }
  .banner-ad {
    position: relative;
    width: 1200px;
    height: 900px;
    box-sizing: border-box;
    border: 16px solid var(--green);
    background: var(--paper);
    overflow: hidden;
    font-family: "Roboto", Arial, sans-serif;
  }
  .backdrop { position: absolute; inset: 0; }
  .backdrop .dark { fill: var(--ink); }
  .backdrop .swoosh { fill: none; stroke: var(--swoosh); stroke-width: 34; }
  .product-photo { fill: url(#photoTone); }

  .warranty-star .star { fill: var(--green); stroke: var(--ink); stroke-width: 4; }
  .warranty-star text {
    fill: var(--ink);
    font-family: "Roboto", Arial, sans-serif;
    font-style: italic;
    font-weight: 900;
    text-anchor: middle;
  }

  .feature .arrow { fill: url(#arrowTone); }
  .feature .arrow-edge { fill: var(--green-dark); }
  .feature .title {
    fill: var(--paper);
    font-style: italic;
    font-weight: 900;
    font-size: 62px;
    text-anchor: middle;
  }
  .feature .subtitle {
    fill: var(--paper);
    font-style: italic;
    font-weight: 700;
    font-size: 32px;
    text-anchor: middle;
  }
</style>
</head>
<body>
<main class="banner-ad">
  <svg class="backdrop" width="1168" height="868" viewBox="16 16 1168 868" xmlns="http://www.w3.org/2000/svg">
    <defs>
      <linearGradient id="photoTone" x1="0" y1="0" x2="1" y2="1">
        <stop offset="0" stop-color="var(--photo-a)"/>
        <stop offset="1" stop-color="var(--photo-b)"/>
      </linearGradient>
      <linearGradient id="arrowTone" x1="0" y1="0" x2="0" y2="1">
        <stop offset="0" stop-color="var(--green-light)"/>
        <stop offset="1" stop-color="var(--green)"/>
      </linearGradient>
    </defs>

    <path class="swoosh" d="M16 708 C250 688 430 630 520 566 C770 410 880 270 915 16"/>
    <path class="dark" d="M915 16 H1184 V884 H16 V708 C250 688 430 630 520 566 C770 410 880 270 915 16 Z"/>

    <path class="product-photo" d="M40 50 H800 V420 H450 V630 H40 Z"
          role="img" aria-label="Photo of two VEKRA Dz340e trials motorcycles, one front view and one side view, white and green with black tyres"/>

    <g class="warranty-star" transform="translate(1015 185) rotate(-8)">
      <polygon class="star" points="0,-205 58,-80 195,-66 92,28 120,165 0,95 -120,165 -92,28 -195,-66 -58,-80"/>
      <g transform="rotate(-16)">
        <text x="-5" y="-10" font-size="118">2</text>
        <text x="10" y="40" font-size="44">years</text>
        <text x="0" y="90" font-size="42">warranty</text>
      </g>
    </g>

    <g class="feature feature-weight">
      <polygon class="arrow-edge" points="520,478 1184,478 1184,582 520,582 468,530"/>
      <polygon class="arrow" points="540,488 1184,488 1184,572 540,572 498,530"/>
      <text class="title" x="840" y="552">light weight</text>
      <text class="subtitle" x="830" y="612">(lightest on the market)</text>
    </g>

    <g class="feature feature-shock">
      <polygon class="arrow-edge" points="436,672 1184,672 1184,776 436,776 384,724"/>
      <polygon class="arrow" points="456,682 1184,682 1184,766 456,766 414,724"/>
      <text class="title" x="790" y="746">BRATTEK rear shock</text>
      <text class="subtitle" x="790" y="808">(Best on the market)</text>
    </g>
  </svg>
</main>
</body>
</html>
```